R&t subterra

We specialize in CIPP pipe lining but do other underground utilities trenchless as well.

Target Market(s)

Trenchless sewer replacement

Contact Information for Business Card

Doug Falvey 715-482-6170 Pinecrest Falls, wi

```html
<!DOCTYPE html>
<html lang="en">
<head>
<meta charset="utf-8">
<title>R&amp;t subterra – Business Card</title>
<link href="https://fonts.googleapis.com/css2?family=Montserrat:wght@400;500;700&display=swap" rel="stylesheet">
<style>
  :root {
    --page-bg: #ecebe8;
    --card-bg: #ffffff;
    --brand-blue: #2e8ecb;
    --ink: #222222;
  }
  * { margin: 0; padding: 0; box-sizing: border-box; }
  html, body {
    width: 1200px; height: 1200px; overflow: hidden;
    background: var(--page-bg);
    font-family: "Montserrat", Arial, sans-serif;
  }
  .canvas { position: relative; width: 1200px; height: 1200px; }
  .card {
    position: absolute;
    background: var(--card-bg); border-radius: 26px;
    box-shadow: 0 6px 18px rgba(0,0,0,0.18);
  }
  .card--front { left: 242px; top: 149px; width: 716px; height: 409px; }
  .card--back { left: 245px; top: 632px; width: 710px; height: 408px; }

  .brand { display: flex; align-items: center; gap: 16px; position: absolute; }
  .brand__dot { border-radius: 50%; background: var(--brand-blue); flex: none; }
  .brand__name { color: var(--brand-blue); font-weight: 700; white-space: nowrap; line-height: 1; }

  .card--front .brand { left: 72px; top: 205px; transform: translateY(-50%); }
  .card--front .brand__dot { width: 56px; height: 56px; }
  .card--front .brand__name { font-size: 29px; }

  .divider {
    position: absolute; left: 393px; top: 140px; width: 2px; height: 131px;
    background: var(--brand-blue);
  }
  .contact__item {
    position: absolute; left: 429px; transform: translateY(-50%);
    color: var(--ink); white-space: nowrap; line-height: 1.2;
  }
  .contact__name { top: 150px; color: var(--brand-blue); font-weight: 700; font-size: 29px; }
  .contact__title { top: 179px; font-size: 19px; font-weight: 400; }
  .contact__line { display: flex; align-items: center; gap: 6px; font-size: 19px; }
  .contact__line--address { top: 222px; }
  .contact__line--phone { top: 263px; }
  .contact__icon { width: 16px; height: 16px; fill: var(--brand-blue); flex: none; }

  .card--back .brand { left: 50%; top: 200px; transform: translate(-50%, -50%); gap: 26px; }
  .card--back .brand__dot { width: 120px; height: 120px; }
  .card--back .brand__name { font-size: 62px; }
</style>
</head>
<body>
<main class="canvas">
  <section class="card card--front">
    <div class="brand">
      <span class="brand__dot"></span>
      <span class="brand__name">R&amp;t subterra</span>
    </div>
    <div class="divider"></div>
    <p class="contact__item contact__name">Doug Falvey</p>
    <p class="contact__item contact__title">Managing Director</p>
    <p class="contact__item contact__line contact__line--address">
      <svg class="contact__icon" viewBox="0 0 24 24" aria-hidden="true"><path d="M12 2a7 7 0 0 0-7 7c0 5.2 7 13 7 13s7-7.8 7-13a7 7 0 0 0-7-7zm0 9.5A2.5 2.5 0 1 1 12 6.5a2.5 2.5 0 0 1 0 5z"/></svg>
      Pinecrest Falls, wi
    </p>
    <p class="contact__item contact__line contact__line--phone">
      <svg class="contact__icon" viewBox="0 0 24 24" aria-hidden="true"><path d="M2 9c0-2 4.5-4 10-4s10 2 10 4v2h-5V9.5c-1.5-.6-3.2-.9-5-.9s-3.5.3-5 .9V11H2zM6 12h12l2 8H4zm4 2v4h4v-4z"/></svg>
      715-482-6170
    </p>
  </section>

  <section class="card card--back">
    <div class="brand">
      <span class="brand__dot"></span>
      <span class="brand__name">R&amp;t subterra</span>
    </div>
  </section>
</main>
</body>
</html>
```